Midwife Poster Ad

I need a poster to go on a wall in my clinic which is in a medical centre shared by doctors and other health professionals. I am a self-employed midwife in New Zealand. I hope for this poster to catch some of the many women who come into the medical centre to have pregnancy tests, see a doctor, or use the pregnancy yoga/pilates services also offered. It will be going on a wall with a bunch of other brochures and ads, so obviously I would like it to stand out and grab their attention as they walk in or out of the centre.

I have attached a few of the images that I currently use in my business cards and brochures. I would like my portrait to feature somewhere on the poster, but does not need to be central. The other images can be used if they work with the design, but are not essential. I would like the poster to include at least one image of a new baby or a pregnant woman/couple.

I would also like a small business card-sized space at the bottom where I can attach a card-holder. I would like the website address to stand out.

The poster should be colourful and communicate the excitement of a new pregnancy.

Target Market(s)

Pregnant women, mothers

Industry/Entity Type

Small Business

Requirements
Must have
• The poster needs to include the following text:
EXPECTING A BABY?
Midwife available here!
Marlene Tobbit LMC Midwife
Clinics run from Kestrel Physio & Pilates
Free pregnancy testing
www.brindlewoodmidwife.co.nz
0215379064

```html
<!DOCTYPE html>
<html lang="en">
<head>
<meta charset="utf-8">
<title>Expecting A Baby? – Marlene Tobbit LMC Midwife</title>
<link rel="stylesheet" href="https://fonts.googleapis.com/css2?family=Play:wght@400;700&family=Open+Sans:wght@400&display=swap">
<style>
  :root {
    --magenta: #b2296f;
    --magenta-light: #c8518b;
    --plum: #6b1450;
    --mauve: #c3a1b6;
    --title-pink: #c9508e;
    --ink: #2e2a2c;
    --muted: #7a7274;
    --panel-top: #ffffff;
    --panel-bottom: #f1d8e6;
    --page: #ffffff;
    --page-edge: #e4e2e2;
  }
  * { box-sizing: border-box; margin: 0; padding: 0; }
  html, body { width: 860px; height: 1200px; overflow: hidden; }
  body {
    position: relative;
    background: radial-gradient(ellipse 70% 55% at 50% 55%, var(--page) 55%, var(--page-edge) 100%);
    font-family: "Open Sans", Arial, sans-serif;
    color: var(--ink);
  }
  .site-invite {
    position: absolute; left: 82px; top: 56px;
    font-size: 15px; color: var(--muted);
  }
  .site-invite .site-name { color: var(--magenta-light); }
  .hero-grid { position: absolute; left: 83px; top: 95px; }
  .headline {
    position: absolute; left: 384px; top: 522px;
    font-family: "Play", "Trebuchet MS", sans-serif; font-weight: 400;
    font-size: 64px; line-height: 58px; letter-spacing: -1px;
    color: var(--title-pink);
  }
  .info-band {
    position: absolute; left: 59px; top: 720px; width: 742px; height: 64px;
    background: var(--magenta);
  }
  .band-heading {
    position: absolute; height: 64px;
    display: flex; align-items: center; justify-content: center;
    font-family: "Play", "Trebuchet MS", sans-serif; font-weight: 700;
    font-size: 19px; color: #fff;
  }
  .band-heading::before {
    content: "›"; position: absolute; left: 16px; font-size: 20px; font-weight: 700;
  }
  .band-heading.about { left: 59px; width: 234px; top: 720px; }
  .band-heading.contact { left: 567px; width: 234px; top: 720px; }
  .feature-panel {
    position: absolute; left: 293px; top: 794px; width: 274px; height: 135px;
    background: linear-gradient(var(--panel-top), var(--panel-bottom));
  }
  .feature-heading {
    position: absolute; left: 293px; top: 712px; width: 274px; height: 82px;
    background: var(--magenta-light);
    box-shadow: 0 3px 8px rgba(0,0,0,0.25);
    display: flex; align-items: center; justify-content: center;
    font-family: "Play", "Trebuchet MS", sans-serif; font-weight: 700;
    font-size: 19px; color: #fff;
  }
  .feature-heading::before {
    content: "›"; position: absolute; left: 36px; font-size: 20px;
  }
  .about-text {
    position: absolute; left: 76px; top: 794px; width: 207px;
    font-size: 14px; line-height: 18.5px; text-align: justify; hyphens: auto;
  }
  .feature-list {
    position: absolute; left: 330px; top: 805px; width: 202px; list-style: none;
    font-size: 14px; line-height: 18.5px;
  }
  .feature-list li { position: relative; padding-left: 26px; margin-bottom: 9px; text-align: justify; }
  .feature-list li::before {
    content: "›"; position: absolute; left: 0; top: -1px;
    color: var(--magenta-light); font-weight: 700; font-size: 16px;
  }
  .contact-details {
    position: absolute; left: 586px; top: 799px;
    font-size: 14px; line-height: 22px;
  }
  .contact-details dd { margin-bottom: 22px; }
</style>
</head>
<body>
  <p class="site-invite">Visit our site at www.<span class="site-name">brindlewoodmidwife</span>.co.nz</p>

  <svg class="hero-grid" width="694" height="554" viewBox="0 0 694 554" role="img" aria-label="Photograph of a newborn baby wrapped in white cloth, lying in a woven basket against a purple backdrop, shown through a grid of tiles">
    <defs>
      <clipPath id="tiles">
        <rect x="0" y="0" width="136" height="136"/><rect x="139" y="0" width="136" height="136"/><rect x="278" y="0" width="136" height="136"/><rect x="417" y="0" width="136" height="136"/><rect x="557" y="0" width="136" height="136"/>
        <rect x="0" y="139" width="136" height="136"/><rect x="139" y="139" width="136" height="136"/><rect x="278" y="139" width="136" height="136"/><rect x="417" y="139" width="136" height="136"/><rect x="557" y="139" width="136" height="136"/>
        <rect x="0" y="278" width="136" height="136"/><rect x="139" y="278" width="136" height="136"/><rect x="278" y="278" width="136" height="136"/><rect x="417" y="278" width="136" height="136"/><rect x="557" y="278" width="136" height="136"/>
        <rect x="0" y="417" width="136" height="136"/><rect x="139" y="417" width="136" height="136"/>
      </clipPath>
      <radialGradient id="subject" cx="0.5" cy="0.5" r="0.5">
        <stop offset="0" stop-color="#f6ece8"/>
        <stop offset="0.6" stop-color="#ead8d8"/>
        <stop offset="1" stop-color="#b07a9e" stop-opacity="0"/>
      </radialGradient>
    </defs>
    <g clip-path="url(#tiles)">
      <rect width="694" height="554" fill="#7a1d5c"/>
      <rect x="139" y="0" width="136" height="136" fill="#c3a1b6"/>
      <rect x="557" y="0" width="136" height="136" fill="#b89aaa"/>
      <rect x="0" y="139" width="136" height="275" fill="#c3a1b6"/>
      <rect x="0" y="0" width="136" height="136" fill="#6b1450"/>
      <rect x="278" y="0" width="136" height="136" fill="#6b1450"/>
      <ellipse cx="360" cy="290" rx="340" ry="210" fill="url(#subject)"/>
      <ellipse cx="430" cy="380" rx="230" ry="90" fill="#9a4a82" opacity="0.35"/>
    </g>
  </svg>

  <h1 class="headline">Expecting A<br>Baby?</h1>

  <div class="info-band"></div>
  <h2 class="band-heading about">About us</h2>
  <h2 class="band-heading contact">Get in touch</h2>

  <div class="feature-panel"></div>
  <h2 class="feature-heading">Midwife available here!</h2>

  <p class="about-text">Having grown up in the city of Tauranga, it is wonderful to be re-establishing my previous Wellington based practice in such a familiar city, I look forward to working closely with local women and their families.</p>

  <ul class="feature-list">
    <li>Clinics run from Kestrel Physio &amp; Pilates</li>
    <li>Marlene Tobbit LMC Midwife</li>
    <li>Free pregnancy testing</li>
  </ul>

  <dl class="contact-details">
    <dt>Phone:</dt>
    <dd>0215379064</dd>
    <dt>Website:</dt>
    <dd>www.brindlewoodmidwife.co.nz</dd>
  </dl>
</body>
</html>
```